NEW YORK Plumbing/utility company 10 year anniversary business card

Looking For simple back and front business card would like to include a few things in description
We offer 24/7 emergency service
residential
commercial
industrial
municipal
services offered
Plumbing
hydro excavation
hydro jetting
Well pumps
Sewer pumps
water mains
sewer mains

```html
<!DOCTYPE html>
<html lang="en">
<head>
<meta charset="utf-8">
<title>Catskill Ridge Water &amp; Sewer – Business Card</title>
<link href="https://fonts.googleapis.com/css2?family=Montserrat:wght@500;600;700;800&display=swap" rel="stylesheet">
<style>
  :root {
    --page-bg: #e7e9ec;
    --navy: #1f4f8f;
    --brand-blue: #2a68a8;
    --deep-blue: #1c3f8c;
    --teal-blue: #3f8fb5;
    --sky: #5fb0d6;
    --card-white: #f3f5f7;
    --faint-mark: #d6e0ea;
    --text-white: #eef6fb;
    --muted-white: #cfe6f2;
  }
  * { box-sizing: border-box; margin: 0; padding: 0; }
  html, body { width: 1200px; height: 900px; overflow: hidden; }
  body {
    background: var(--page-bg);
    font-family: "Montserrat", sans-serif;
    display: flex;
    flex-direction: column;
    align-items: center;
    justify-content: center;
    gap: 36px;
  }
  .card {
    position: relative;
    width: 720px;
    height: 411px;
    overflow: hidden;
    box-shadow: 0 8px 24px rgba(0,0,0,0.18);
  }

  /* ---------- Back (blue) ---------- */
  .card-back {
    background: linear-gradient(120deg, var(--brand-blue) 0%, var(--teal-blue) 55%, var(--sky) 100%);
    color: var(--text-white);
  }
  .card-back .arc { position: absolute; inset: 0; }
  .back-info { position: absolute; left: 48px; top: 40px; width: 360px; }
  .back-info .company { font-size: 27px; font-weight: 600; letter-spacing: 1px; }
  .back-info .tagline { font-size: 11px; font-weight: 600; letter-spacing: 2px; margin-top: 2px; color: var(--muted-white); }
  .back-info .phone { font-size: 22px; font-weight: 700; margin-top: 10px; letter-spacing: 1px; }
  .back-info .email { font-size: 14px; font-weight: 500; margin-top: 4px; color: var(--muted-white); }
  .back-block { margin-top: 22px; }
  .back-block h3 { font-size: 15px; font-weight: 700; margin-bottom: 8px; }
  .back-block .lists { border-left: 2px solid var(--text-white); padding-left: 10px; display: flex; gap: 40px; }
  .back-block ul { list-style: none; font-size: 10px; font-weight: 600; line-height: 1.45; }
  .back-block li::before { content: "– "; }
  .back-name {
    position: absolute; right: 72px; top: 214px; width: 240px; text-align: center;
    color: var(--deep-blue); font-size: 44px; font-weight: 800; letter-spacing: 2px;
  }
  .back-name small { display: block; font-size: 14px; font-weight: 800; letter-spacing: 1.5px; }

  /* ---------- Front (white) ---------- */
  .card-front { background: var(--card-white); color: var(--navy); }
  .faint-mark {
    position: absolute; left: 40px; top: 130px;
    font-size: 290px; font-weight: 800; letter-spacing: 10px; line-height: 1;
    color: var(--faint-mark);
  }
  .front-brand { position: absolute; left: 30px; top: 26px; display: flex; align-items: center; gap: 10px; }
  .front-brand .dot { width: 26px; height: 26px; border-radius: 50%; background: var(--brand-blue); }
  .front-brand .name { font-size: 30px; font-weight: 800; color: var(--brand-blue); letter-spacing: 2px; }
  .front-contact { position: absolute; right: 34px; top: 28px; text-align: center; width: 330px; }
  .front-contact .company { font-size: 22px; font-weight: 600; letter-spacing: 1px; color: var(--brand-blue); }
  .front-contact .tagline { font-size: 11px; font-weight: 600; letter-spacing: 1.5px; margin-top: 2px; }
  .front-contact .phone { font-size: 19px; font-weight: 700; margin-top: 10px; letter-spacing: 1px; }
  .front-contact .email { font-size: 13px; font-weight: 500; margin-top: 4px; color: var(--brand-blue); }
  .front-block { position: absolute; top: 260px; }
  .front-block.coverage { left: 28px; }
  .front-block.services { left: 390px; top: 280px; }
  .front-block h3 { font-size: 13px; font-weight: 700; color: var(--brand-blue); margin: 0 0 8px 30px; }
  .front-block .lists { border-left: 2px solid var(--navy); padding-left: 12px; display: flex; gap: 36px; }
  .front-block ul { list-style: none; font-size: 9.5px; font-weight: 700; line-height: 1.45; letter-spacing: 0.5px; }
  .front-block li::before { content: "– "; }
</style>
</head>
<body>

  <section class="card card-back">
    <svg class="arc" width="720" height="411" viewBox="0 0 720 411" aria-hidden="true">
      <circle cx="640" cy="330" r="300" fill="#2a4fa0"/>
      <circle cx="640" cy="330" r="262" fill="#f1f3f6"/>
    </svg>
    <div class="back-info">
      <div class="company">CATSKILL RIDGE</div>
      <div class="tagline">WATER &amp; SEWER</div>
      <div class="phone">845-555-0182</div>
      <div class="email">info@CRWSNY.com</div>
      <div class="back-block">
        <h3>We offer 24/7 emergency service</h3>
        <div class="lists">
          <ul><li>RESIDENTIAL</li><li>COMMERCIAL</li></ul>
          <ul><li>INDUSTRIAL</li><li>MUNICIPAL</li></ul>
        </div>
      </div>
      <div class="back-block">
        <h3>Services offered</h3>
        <div class="lists">
          <ul><li>PLUMBING</li><li>HYDRO EXCAVATION</li><li>HYDRO JETTING</li><li>WELL PUMPS</li></ul>
          <ul><li>SEWER PUMPS</li><li>WATER MAINS</li><li>SEWER MAINS</li></ul>
        </div>
      </div>
    </div>
    <div class="back-name">CRW<small>CATSKILL RIDGE</small></div>
  </section>

  <section class="card card-front">
    <div class="faint-mark" aria-hidden="true">CRW</div>
    <div class="front-brand"><span class="dot"></span><span class="name">CRW</span></div>
    <div class="front-contact">
      <div class="company">CATSKILL RIDGE</div>
      <div class="tagline">WATER &amp; SEWER</div>
      <div class="phone">845-555-0182</div>
      <div class="email">info@CRWSNY.com</div>
    </div>
    <div class="front-block coverage">
      <h3>We offer 24/7 emergency service</h3>
      <div class="lists">
        <ul><li>RESIDENTIAL</li><li>COMMERCIAL</li></ul>
        <ul><li>INDUSTRIAL</li><li>MUNICIPAL</li></ul>
      </div>
    </div>
    <div class="front-block services">
      <h3 style="margin-left:80px">Services offered</h3>
      <div class="lists">
        <ul><li>PLUMBING</li><li>HYDRO EXCAVATION</li><li>HYDRO JETTING</li><li>WELL PUMPS</li></ul>
        <ul><li>SEWER PUMPS</li><li>WATER MAINS</li><li>SEWER MAINS</li></ul>
      </div>
    </div>
  </section>

</body>
</html>
```